My Professional Resume/CV Design

Hi Pixel Harbor experts, I need a professional resume/CV design for using my carrier hiring activities. I have a draft and this draft is 2 types.
1) Traditional IT Major Company Senior(Manager Level) to Director level application (File: Tanabe_Emiko_Res_EN2023AprA)
>Application example companies: Velmora, Drakt, Quindle, Brightmarsh, HoltenWare, Fenwick Ridge, Zentravix, Morivon, Quorexa, Plinth, dZop, Kelvarna etc
>This should not be fancy. Please make format with traditional/gentle/standard but also need to appear unique point such as icons, borderlines etc
2) Cutting-Edge (Web 3.0/metaverse/NFT/Crypto) Start-up or Young (Less 5 year's history) Company Director and C-Levels position application (Tanabe_Emiko_Res_EN2023Apr_typeC)
>Application Example Companies: Tessaluk Studios, Vorlexa, Zintaro.example, Wovenpath, Lumbrook, FernPocket, Thaxel, Kipa/Dult/Snov, Morvik, QUESTAN, wordLYM etc
>This resume format should be something "edge" "advanced" "future" and "high-tech", so need to your high sense of design technics.
Both drafts is without a profile picture, but I need to put in my portfolio picture (Just attached one is my 2018's, you can trim and edit as well)
For the document format, please send me to WORD and PAGES both. and total MAX 2 page in all contents please (No more 3 pages)
Target Market(s)
Traditional Major Tech Company's VP/Directors or/and Latest Web 3.0 StartUp C-Levels (CEO/CTO/CSO/COO etc)
Industry/Entity Type
Technology
Font styles to use
Other font styles liked:
- Choose 3 a)Century Gothic b) Avenir c)Graphik d)Kohinoor e)Optima f)Platino
Look and feel
Each slider illustrates characteristics of the customer's brand and the style your logo design should communicate.

```html
<!DOCTYPE html>
<html lang="en">
<head>
<meta charset="utf-8">
<title>Emiko Tanabe – Resume</title>
<link href="https://fonts.googleapis.com/css2?family=Tinos:ital,wght@0,400;0,700;1,700&family=Roboto+Condensed:ital,wght@0,400;0,700;1,400&family=Open+Sans:wght@400&display=swap" rel="stylesheet">
<style>
:root{
  --backdrop:#e6e6e6;
  --paper:#ffffff;
  --navy:#1f4e79;
  --black:#000000;
  --ink:#161616;
  --band-gray:#d9d9d9;
  --rule:#555555;
  --job-band:#dce6f1;
  --bullet-blue:#2e75b6;
  --photo-a:#6d7f92;
  --photo-b:#2a2f3a;
}
*{box-sizing:border-box;margin:0;padding:0}
html,body{width:1200px;height:945px;overflow:hidden;background:var(--backdrop)}
body{position:relative;font-family:"Roboto Condensed",Arial,sans-serif;color:var(--ink)}
.page{position:absolute;width:570px;height:738px;background:var(--paper);padding:0 35px;overflow:hidden;box-shadow:0 2px 8px rgba(0,0,0,.18)}
.page-one{left:20px;top:103px}
.page-two{left:610px;top:103px}

.masthead{position:relative;height:116px;background:var(--navy)}
.portrait{position:absolute;left:26px;top:41px;width:86px;height:86px;border-radius:50%;background:radial-gradient(circle at 50% 40%,var(--photo-a),var(--photo-b))}
.name{position:absolute;left:160px;top:50px;font-family:Tinos,serif;font-weight:700;font-size:20px;letter-spacing:.5px;color:#fff}
.location{position:absolute;left:160px;top:74px;font-family:Tinos,serif;font-size:7.5px;color:#fff}
.contact-bar{height:16px;background:var(--black);color:#fff;font-family:"Open Sans",sans-serif;font-size:7px;line-height:16px;padding-left:160px}
.running-head{height:28px;background:var(--navy);color:#fff;font-family:"Open Sans",sans-serif;font-size:6.3px;line-height:28px;text-align:center;margin-bottom:8px}

.headline{background:var(--band-gray);border-top:1px solid var(--rule);border-bottom:1px solid var(--rule);text-align:center;font-family:Tinos,serif;padding:2px 0 1px;margin-top:3px}
.headline .roles{font-weight:700;font-size:7.6px;letter-spacing:.2px}
.headline .tagline{font-weight:700;font-style:italic;font-size:7.2px}
.section-title{background:var(--band-gray);border-top:1px solid var(--rule);border-bottom:1px solid var(--rule);text-align:center;font-family:Tinos,serif;font-weight:700;font-size:7.8px;letter-spacing:.3px;padding:1px 0;margin:8px 0 4px}
.section-title small{font-weight:400;font-size:5.8px;letter-spacing:0}

p,li{font-size:6.3px;line-height:1.5}
.summary{margin-top:3px;text-align:justify}
.summary strong{font-weight:700}

.highlights{list-style:none;padding-left:26px}
.highlights li{position:relative;text-align:justify;margin-bottom:2px}
.highlights li::before{content:"";position:absolute;left:-15px;top:3.5px;width:2.5px;height:2.5px;border-radius:50%;background:var(--bullet-blue)}

.competencies{display:grid;grid-template-columns:repeat(3,1fr);row-gap:1px;list-style:none;padding-left:6px;margin-top:2px}
.competencies li{position:relative;padding-left:16px;line-height:1.9}
.competencies li::before,.duties li::before{content:"";position:absolute;left:0;top:4px;width:2.5px;height:2.5px;border-radius:50%;background:var(--ink)}

.job{margin-top:6px}
.job-head{display:flex;justify-content:space-between;background:var(--job-band);font-family:Tinos,serif;font-weight:700;font-size:7.6px;padding:0 2px;margin-bottom:1px}
.job p{text-align:justify}
.duties{list-style:none;padding-left:34px;margin-top:3px}
.duties li{position:relative;margin-bottom:1px}
.duties li::before{left:-16px}
.duties.tight{padding-left:17px}
.duties.tight li::before{left:-14px}
.sub-head{text-decoration:underline}
.sub-body{padding-left:10px}
.note{font-style:italic;font-size:5.9px}
.education-line{text-align:center;font-weight:700;font-size:6.3px;margin-top:5px}
</style>
</head>
<body>

<section class="page page-one">
  <header class="masthead">
    <div class="portrait" role="img" aria-label="Portrait photo of the candidate"></div>
    <h1 class="name">EMIKO TANABE</h1>
    <p class="location">Wanchai, Hong Kong</p>
  </header>
  <div class="contact-bar">etanabe512@mailbox.example &nbsp;| &nbsp;+852 5550 0148</div>

  <div class="headline">
    <div class="roles">BUSINESS DEVELOPMENT | CUTTING EDGE TECHNOLOGY | PARTNER CHANNEL SALES</div>
    <div class="tagline">Wide-Range Propose Ability / Strategic Planning &amp; Execution / Be As a Professional Middleman between Japan/APAC/Global</div>
  </div>

  <p class="summary">My value and career will only increase in a diverse and multinational work environment. High-impact growth-oriented professional demonstrating a strong grasp of current marketing tools and strategies aligned with cutting-edge technology, with an interest in the transformation of society/era events within the industry and cyber security, with an Entrepreneurial spirit. Strategically collaborate with external vendors and internal business partners; manages various commercial platforms, systems, domains, and channels to ensure scale marketing and lead development capabilities in line with business growth plans that deliver high-quality results. Participate in supply chain strategy development, developing implementation plans, and methods of dealing with business. Display strong analytical ability to evaluate end-to-end customer experience across multiple channels and customer touchpoints. Highly creative with experience in identifying target audiences and devising digital campaigns while valuing traditional methods that engage, inform, and motivate while staying abreast of industry trends.<br>“<strong>Cutting-Edge Technologies” “Business Development” and “Japan/APAC Channel Sales”</strong> are my main core.</p>

  <h2 class="section-title">HIGHLIGHTS OF QUALIFICATION</h2>
  <ul class="highlights">
    <li>As Bridge to the gap of Japanese business culture faced by many non-Japanese companies. The Japanese market is potentially huge and digital transformation is lagging behind, there is a lot of opportunities to take a market share. Most of their weakness is “Culture Difference” rather than “language”, I am a native Japanese, fluent English Speaker, and as a business developer is familiar with business practices in Japan/other than Japan, I have confidence fulfill the role of mutual understanding</li>
    <li>Expert in conducting marketing research and analyzing data strategically to identify brand / product value proposition, prospect customers, markets, and major competitors while utilizing PM software (visualization with 5W1H details)</li>
    <li>Understands target audiences and competition dynamics with insights from the various premise sources while leading integrated digital and offline marketing campaigns from concept to execution, on time and within scope and budget.</li>
    <li>Serve as supply chain interfaces for all major projects, with clear knowledge in project progress, logistics and distribution development consideration with each customer journey, and implementation and execution from upper to lower streams.</li>
    <li>Conceptualize and develop brand/product marketing plans and campaigns for companies and individual business lines, including planning, liaison, coordination and execution.</li>
  </ul>

  <h2 class="section-title">CORE COMPETENCIES</h2>
  <ul class="competencies">
    <li>Global Operations Management</li><li>Key Account Management</li><li>Staff Training / Retention</li>
    <li>Strategic Partnerships</li><li>Business Restructuring</li><li>Business Administration</li>
    <li>Process Improvement Champion</li><li>Team Leadership / Management</li><li>Supply Chain &amp; Logistics</li>
    <li>Strategic Planning &amp; Execution</li><li>P &amp; L / Revenue Growth</li><li>Vendor / Financial Management</li>
    <li>Cryptocurrency | B2B &amp; B2C</li><li>Budget Management</li><li>Negotiations &amp; Agreements</li>
    <li>Research &amp; Development</li><li>Sales B2B + B2G</li><li>Records &amp; Documentation</li>
  </ul>

  <h2 class="section-title">PROFESSIONAL EXPERIENCE <small>(&amp; *Reason for Leaving write end of each carrier paragraph)</small></h2>

  <article class="job">
    <div class="job-head"><span>Inside Renewals Sales | Keltwater Networks. | Hong Kong |</span><span>Jul 2022 - Present</span></div>
    <p>First visa-sponsored employee since the establishment of the APAC Hong Kong company (2017 and in total over 100+). Promotion to Territory Manager (Inside New Sales) is factored in. The agreement to start with renewal sales was to be able to build relationships with existing partners and to set the stage for the new position. Due to internal circumstances, there is no budgetary visibility for an Inside Sales Manager for the Japan Territory. Job hunting activity while still employed for reasons of wanting to advance own careers external, as prospects for promotion within the company are very low expectations by company reasons.</p>
    <ul class="duties">
      <li>Distributor and Reseller (Partner) Management: Before I join, Keltwater was the low position for any of the partner's sales, like quotation production due to only focused PO. I focusing what end users face on the problems and pain and shared with proper partners. A result, they never ask me for a quotation (they now can quote themself) and they proposed me to new sales plans and strategies. I just concentrated to do what my partner want and relationship development.</li>
      <li>Co-work with Territory Regional Team remotely: Mainly Japan Sales, SEs, CS, Technical Support</li>
      <li>Enhancing mutual synergies with other regional teams: Corporate team works with especially APAC another region team ( India/SEA/ANZ/China total 4 regions) and US and EMEA as well.</li>
    </ul>
  </article>

  <article class="job">
    <div class="job-head"><span>Business Development Manager | Orvane HK Limited | Hong Kong</span><span>Apr 2021- Apr 2022</span></div>
    <p>Join from GM's direct invitation because he wants to survive the pandemic crisis, this is an IT reseller business provider in Hong Kong, China, SEA, and Japan market. Upon long-term mainly prospective business development and strategy, then proposed better to downsizing and restructuring inclusive me, I suggest leaving this company and GM accepted (Still best relationships).</p>
  </article>
</section>

<section class="page page-two">
  <div class="running-head">EMIKO TANABE | ETANABE512@MAILBOX.EXAMPLE | +852 5550 0148</div>

  <ul class="duties tight">
    <li><span class="sub-head">As a Management Strategy and Business Development</span><br>Proposed various restructuring options including M&amp;A, collaboration with the competitors, high demanded IT solutions, Web Marketing campaigns especially for sleeping existing customers reclamation (Company running 30 years)</li>
    <li><span class="sub-head">Daily Operation as a CRM/Sales/Key Accounting</span><br><span class="sub-body">“One Stop Solutions” expert and salesperson as a 100+ client's information systems department. Providing 6 core IT-related services to located at both Hong Kong and China mainland B2B/ B2G based customers with respect and according to their requirements, corporate culture, size, nature, and policies.</span></li>
    <li><span class="sub-head">Involvement with client VC advisory service.</span><br><span class="sub-body">Seeking potential cutting-edge technology or software-related start-ups. Or performing technical due diligence and making judgments on the product of companies presented by the client-side for operating the best portfolio.</span></li>
  </ul>

  <article class="job">
    <div class="job-head"><span>Advisor of Business Development| Rennic High-Tech (Hong Kong) Limited | Hong Kong</span><span>May 2020 – Mar 2021</span></div>
    <p>I joined the company after contacting the person responsible for developing a medical digital device to prevent the COVID-19 pandemic and presenting the business to the company to achieve commercial success.</p>
    <ul class="duties tight">
      <li><span class="sub-head">Business development of organic disinfectant water creation devices</span><br><span class="sub-body">A new generation of organic disinfectant devices was launched at a part of medical places in Japan. Producing disinfectant water only with tap water and replacing alcohol. In order to bring the organization from being a group of developers to commercial professionals, various operations were required. Since a basic framework generates, the necessary tasks are identified, responsibilities were allocated to a proper person in charge, a business plan was drawn up with a rough timeline and scenario.<br>Due to a change in policy, which focuses on commercial success in Japan before the Asian and global markets, I am no longer heavy responsibility for the project and am now involved just as a non-accountable advisor.</span></li>
      <li><span class="sub-head">Business Development of new flying mobility start-up</span><br><span class="sub-body">Development of a business plan for the production and development of the new Flying Mobility, the brainchild of the company's president. I've left this and hand over to the proper person such as the financial department for fundraising.</span></li>
    </ul>
    <p class="note">*Low expectations that the fundraising would be executed quickly, and a headhunting request from the GM of Orvane HK Limited</p>
  </article>

  <article class="job">
    <div class="job-head"><span>Business Development Manager | Sorrel Global | Hong Kong</span><span>Apr2019 –Mar 2020</span></div>
    <p>Demonstrate mastery in the production of a new TV program with Gulfline National News Agency (TV station) for introducing cutting-edge science such as human-type robots; creating program/production budgets and completed all interactions with the research institute on behalf of the TV station and also planned the 12 episodes of the first episode</p>
    <ul class="duties tight">
      <li>Spearhead Japan and China's incorporation in the investigation and introduction of cutting-edge technology to which enhanced operational productivity and efficiency for Gulfline partners.</li>
      <li>In the Ministry of IT Gulfline, presented Humanoid robotics usage for TV presenter collaborated with Gulfline TV directors.</li>
    </ul>
    <p class="note">*Having received notification that funding from the Gulfline government has been frozen for six months due to the pandemic</p>
  </article>

  <article class="job">
    <div class="job-head"><span>Head of Division | Quarry9 Tech Limited (Ashgrove Group (Holdings) Ltd. | Hong Kong</span><span>May 2016 – Mar 2019</span></div>
    <p>Started work as one of the key players of Fin-Tech industry, Management, and head of operations of a platform for digital assets. When I first joined the company, it was just me as a junior manager + the CEO means actual 1 staff number, by 2018, the FinTech division had grown to 15 people in the Hong Kong office, over 100 people in total including BPO partners in Japan, the Philippines, Netherlands, etc. In this two-year period, I have achieved a total of 4 promotions and achieved my working carrier breakthroughs.</p>
    <ul class="duties tight">
      <li>Outperformed corporate expectations in leading and supervising digital asset white label exchange operations by improving systems that cannot be managed before I join and implementing process improvement initiatives and manuals.</li>
      <li>Adept in managing multiple projects, achieving stable operational exchange, contributing to end-user increase from 1.5K to 5K.</li>
      <li>Nominated Taiwan subsidiary head of a startup, between May to Oct 2017, Spearhead global business operations while overseeing the Taiwan subsidiary business expansion to Taiwanese partner b2b clients and handover to the local manager.</li>
      <li>Pioneered customized Digital Asset Exchange platform, process improvement initiatives, facilitating prompt delivery to clients.</li>
      <li>Delivering digital assets to clients using exceptional customer service management to generate business while facilitating customers' integration wallet and listing exchange for each industry's digital asset. Total fund-raising amount was over US$ 1B.</li>
      <li>Displayed solid leadership abilities in team-building / mentoring activities and optimized project branding processes involving HR oversight and staffing as well as financial control for each project.</li>
    </ul>
    <p class="note">*As I could not expect any further promotion, I transfer to further develop my career and gain multi-national business acumen.</p>
  </article>

  <article class="job">
    <div class="job-head"><span>Project Manager | PT. KIRANA LESTARI | Tokyo &amp; Denpasar</span><span>2014 – 2015</span></div>
    <ul class="duties tight">
      <li>Possessed a stellar review in the strategic planning of corporate projects with B2B institutions at Bali of Indonesia Microfinance and Property Corporate.</li>
    </ul>
    <p class="note">*Relocate to Hong Kong by my personal reason at the time late of 2015</p>
  </article>

  <article class="job">
    <div class="job-head"><span>Chief Operation Officer | Meridia Agency | Tokyo</span><span>2010 – 2014</span></div>
    <ul class="duties tight">
      <li>Structured and pioneered the process of running the Tokyo branch of a Singaporean restaurant by connecting with the F&amp;B company. Demonstrated strength in PR including the English Media to increase brand awareness and clientele growth.</li>
    </ul>
    <p class="note">*The business cessation requirements of the JV Agreement are met. (Reason cannot be given due to confidentiality, but I can answer orally.)</p>
  </article>

  <h2 class="section-title">EDUCATION</h2>
  <p class="education-line">Bachelor's Degree in Economics/Philosophy | University of Hoshimi, Japan</p>
</section>

</body>
</html>
```